Non-profit, faith-based, and other local community organizations. We are initiating a New Member Campaign so these would be used to generate interest and awareness about joining the Co-Op. Emphasizing the benefits of our services and how it would help their organizations.
Be creative but maintain a simple and sophisticated look. Blue and charcoal is preferred coloring but not absolute. Community based pictures and ones symbolizing "Membership is the Heart" are preferred. Trying to display a trusted, local, and service oriented image. Please refer to our website at www.bramwellco-op.org to get a better feel.
quelvrid quelvrid
BramwellCooperative BramwellCooperative
I would prefer not to use world or country images as we are trying to have a "local" perception.
Draft #9: The overall layout is good however I prefer to keep the logo intact instead splitting the "Bramwell Co-Op" to the side. When as is, it provides an abstract tree image which goes along with our sustainability focus. Also, I prefer the logo being more of the focal point instead of the tagline "Membership is the Heart". Thanks
Lamp42 and Ostvelk: Thanks for your submissions. If you are able to create drafts without the text appearing so heavy, I would appreciate it. Having the front and back flaps displaying more contact info is also preferred.
Can other photos such as Pixvault examples 20473615 (Membership Heart) and 30914762 (Community puzzle) be used as opposed to the website photos? These are just suggestions and if other photos displaying similar meaning can be found, great. Thanks,
Draft #6: I like the creativity and the eye appealing layout. I definitely prefer NOT having the text be the focal point and become too overbearing for the audience. Are you able to use other pictures as mentioned in the following comments?

```html
<!DOCTYPE html>
<html lang="en">
<head>
<meta charset="utf-8">
<title>Bramwell Co-Op — New Member Brochure</title>
<link href="https://fonts.googleapis.com/css2?family=Open+Sans:wght@400;600;700;800&display=swap" rel="stylesheet">
<style>
:root{
  --backdrop:#2a2426;
  --blue:#1f6fb2;
  --blue-deep:#17578f;
  --blue-light:#3a8fd6;
  --charcoal:#3b3d42;
  --gray:#d9dadd;
  --gray-soft:#eceded;
  --ink:#4a4c51;
  --white:#ffffff;
}
*{box-sizing:border-box;margin:0;padding:0}
html,body{width:1200px;height:902px;overflow:hidden}
body{background:var(--backdrop);font-family:"Open Sans",Arial,sans-serif;color:var(--ink);position:relative}
.sheet{position:absolute;background:var(--white);box-shadow:0 4px 14px rgba(0,0,0,.5);overflow:hidden}
.panel{position:absolute;top:0;bottom:0;overflow:hidden}
.photo{position:absolute}
.band{background:var(--blue);color:var(--white)}
.logo{display:flex;align-items:center;gap:6px;justify-content:center}
.logo .dot{width:14px;height:14px;border-radius:50%;background:var(--charcoal)}
.logo .name{font-weight:700;color:var(--charcoal);letter-spacing:.5px;white-space:nowrap}
.tiny{font-size:5.6px;line-height:1.45}
.small{font-size:6.5px;line-height:1.45}
.benefit h4{font-size:7px;font-weight:700;color:var(--white);background:var(--charcoal);padding:3px 5px 3px 18px;position:relative;text-transform:uppercase;letter-spacing:.4px;white-space:nowrap}
.benefit h4 svg{position:absolute;left:4px;top:2px}
.benefit p{font-size:5.6px;line-height:1.5;padding:4px 5px 7px}
.list-item{font-size:7px;font-weight:700;color:var(--charcoal);text-transform:uppercase;letter-spacing:.6px;padding:7px 10px;border-bottom:1px solid #bfc1c5}
.badge{width:46px;height:22px;background:#b9bcc1;border-radius:3px}
.benefits-heading{font-size:12px;font-weight:700;color:var(--blue);line-height:1.25}
</style>
</head>
<body>

<!-- Left sheet, outside spread -->
<section class="sheet outside" style="left:24px;top:19px;width:612px;height:401px">
  <div class="panel back-flap" style="left:0;width:204px">
    <div class="photo" role="img" aria-label="Photo of many hands stacked together in unity" style="left:0;top:0;width:204px;height:118px;background:linear-gradient(135deg,#c9a98c,#8a6b58 60%,#5e6b76)"></div>
    <div class="band" style="position:absolute;top:118px;left:0;right:0;height:70px;padding:12px 14px">
      <p style="font-size:8px;font-weight:700;line-height:1.35">An annual membership fee of $100 includes all of these features and more.</p>
    </div>
    <div style="position:absolute;top:196px;left:14px;right:14px">
      <p class="small">For more information or how we can provide assistance, please visit our website:</p>
      <p class="small" style="font-weight:700;color:var(--blue);margin:2px 0 10px">www.bramwellco-op.org</p>
      <p class="small">Call us at:</p>
      <p style="font-size:9px;font-weight:700;color:var(--charcoal);margin-bottom:8px">(555) 201-4470</p>
      <p class="small">Email us at:</p>
      <p class="small" style="font-weight:700;color:var(--blue)">info@bramwellco-op.org</p>
    </div>
    <div style="position:absolute;bottom:0;left:0;right:0;height:72px;background:var(--gray-soft);padding:14px">
      <p style="font-size:8.5px;font-weight:800;color:var(--charcoal);line-height:1.35">We look forward to welcoming you into our cooperative community!</p>
    </div>
  </div>

  <div class="panel mailer" style="left:204px;width:204px;border-left:1px solid #e2e3e5;border-right:1px solid #e2e3e5">
    <div class="logo" style="position:absolute;top:42px;left:0;right:0;flex-direction:column;gap:8px">
      <span class="dot" style="width:46px;height:46px"></span>
      <span class="name" style="font-size:15px">Bramwell Co-Op</span>
    </div>
    <div style="position:absolute;top:178px;left:14px;right:14px;background:var(--gray-soft);padding:10px">
      <p class="small" style="font-weight:700;color:var(--charcoal)">Bramwell Cooperative, Inc.</p>
      <p class="small">240 Hollis Way</p>
      <p class="small">Larkfield, PA 10000</p>
      <p class="small" style="margin-top:6px">Phone: (555) 201-4470</p>
      <p class="small">Fax: (555) 201-4471</p>
      <p class="small">Email: info@bramwellco-op.org</p>
    </div>
    <div style="position:absolute;top:300px;left:14px;right:14px">
      <p style="font-size:7px;font-weight:700;color:var(--charcoal);letter-spacing:.6px;margin-bottom:8px">MEMBER OF:</p>
      <div style="display:flex;justify-content:space-between"><span class="badge"></span><span class="badge"></span><span class="badge"></span></div>
    </div>
  </div>

  <div class="panel front-cover" style="left:408px;width:204px">
    <div class="photo" role="img" aria-label="Photo of hands joining puzzle pieces representing community" style="left:0;top:0;width:204px;height:96px;background:linear-gradient(120deg,#7f9fbf,#d6dde4 50%,#9aa7b3)"></div>
    <div class="band" style="position:absolute;top:96px;left:0;right:0;height:22px;padding:6px 10px;font-size:6.5px;font-weight:700;letter-spacing:.6px">BRINGING OUR COMMUNITY TOGETHER</div>
    <div style="position:absolute;top:118px;left:0;right:0;background:var(--gray)">
      <div class="list-item">Sustainability</div>
      <div class="list-item">Collaboration</div>
      <div class="list-item">Community</div>
      <div class="list-item" style="border:none">Solutions</div>
    </div>
    <div style="position:absolute;top:240px;left:14px;right:14px">
      <p class="small">Supporting local non-profit, faith-based and community groups with shared services, savings and trusted guidance since our founding.</p>
    </div>
    <p style="position:absolute;bottom:14px;left:0;right:0;text-align:center;font-size:7px;font-weight:700;color:var(--blue)">www.bramwellco-op.org</p>
  </div>
</section>

<!-- Left sheet, inside spread -->
<section class="sheet inside" style="left:24px;top:444px;width:612px;height:439px">
  <div class="panel" style="left:0;width:204px">
    <div class="logo" style="position:absolute;top:22px;left:0;right:0;flex-direction:column;gap:6px">
      <span class="dot" style="width:36px;height:36px"></span>
      <span class="name" style="font-size:13px">Bramwell Co-Op</span>
    </div>
    <div class="band" style="position:absolute;top:104px;left:0;right:0;height:22px;padding:5px 12px;font-size:8.5px;font-weight:700;letter-spacing:.4px">MEMBERSHIP IS THE HEART</div>
    <div style="position:absolute;top:134px;left:12px;right:12px">
      <p class="tiny">Bramwell Co-Op helps strong local organizations grow stronger. By pooling purchasing power, we give members access to savings and services that would be hard to reach alone.</p>
      <p class="tiny" style="margin-top:5px">Our members shape everything we do. Each voice guides the programs we offer, the partners we choose and the way we serve our neighbors across the region.</p>
      <p class="tiny" style="margin-top:5px">Joining means more time for your mission and less time on paperwork, billing and supply questions. We handle the details so you can focus on people.</p>
    </div>
    <div class="photo" role="img" aria-label="Photo of a glowing sphere held in open hands, symbolizing the heart of membership" style="left:0;bottom:0;width:204px;height:112px;background:radial-gradient(circle at 50% 55%,#cfe4f5,#4b8cc4 45%,#1c3f63)"></div>
  </div>

  <div class="panel" style="left:204px;width:204px;border-left:1px solid #e2e3e5;border-right:1px solid #e2e3e5">
    <h2 class="benefits-heading" style="position:absolute;top:24px;left:12px;right:12px">Some of the benefits that we can offer you include...</h2>
    <div style="position:absolute;top:86px;left:10px;right:10px">
      <div class="benefit">
        <h4><svg width="10" height="10" viewBox="0 0 10 10"><circle cx="5" cy="5" r="4.5" fill="#3a8fd6"/><path d="M3 5.2l1.4 1.4L7.2 3.6" stroke="#fff" stroke-width="1.2" fill="none"/></svg>Membership Discounts</h4>
        <p>The buying leverage of the co-op's members lets us negotiate lower prices on office supplies, insurance, utilities and everyday services. Savings are passed directly to every member organization.</p>
      </div>
      <div class="benefit">
        <h4><svg width="10" height="10" viewBox="0 0 10 10"><circle cx="5" cy="5" r="4.5" fill="#3a8fd6"/><path d="M3 5.2l1.4 1.4L7.2 3.6" stroke="#fff" stroke-width="1.2" fill="none"/></svg>Bill Consolidation</h4>
        <p>One simple monthly statement replaces a pile of separate vendor bills. Your staff spend less time on accounts and more time on the work that matters to your community.</p>
      </div>
    </div>
    <div class="photo" role="img" aria-label="Photo of fresh green grass under a clear sky" style="left:0;bottom:0;width:204px;height:110px;background:linear-gradient(180deg,#cfe3f3,#9cc6e6 40%,#7fb545 62%,#4f8a26)"></div>
  </div>

  <div class="panel" style="left:408px;width:204px">
    <div style="position:absolute;top:24px;left:10px;right:10px">
      <div class="benefit">
        <h4><svg width="10" height="10" viewBox="0 0 10 10"><circle cx="5" cy="5" r="4.5" fill="#3a8fd6"/><path d="M3 5.2l1.4 1.4L7.2 3.6" stroke="#fff" stroke-width="1.2" fill="none"/></svg>Operational Resources</h4>
        <p>Members can draw on shared training, templates and expert guidance for budgeting, facilities and staffing. Our team is a phone call away whenever you need help planning ahead.</p>
      </div>
      <div class="benefit" style="margin-top:10px">
        <h4><svg width="10" height="10" viewBox="0 0 10 10"><circle cx="5" cy="5" r="4.5" fill="#3a8fd6"/><path d="M3 5.2l1.4 1.4L7.2 3.6" stroke="#fff" stroke-width="1.2" fill="none"/></svg>Sustainability</h4>
        <p>We help members lower energy use and waste through practical programs and trusted local partners. Greener choices save money and care for the place we all call home.</p>
      </div>
      <div class="benefit" style="margin-top:10px">
        <h4><svg width="10" height="10" viewBox="0 0 10 10"><circle cx="5" cy="5" r="4.5" fill="#3a8fd6"/><path d="M3 5.2l1.4 1.4L7.2 3.6" stroke="#fff" stroke-width="1.2" fill="none"/></svg>Annual Rebate</h4>
        <p>At the end of each fiscal year, surplus earnings are shared with members as a rebate based on participation. The more you use the co-op, the more you receive back.</p>
      </div>
    </div>
  </div>
</section>

<!-- Right sheet, single page -->
<section class="sheet flyer" style="left:667px;top:53px;width:509px;height:811px">
  <div class="photo" role="img" aria-label="Photo of community members joining hands" style="left:0;top:0;width:509px;height:150px;background:linear-gradient(120deg,#b89a80,#d9c6b5 40%,#7d98b4 75%,#4d6f93)"></div>
  <div style="position:absolute;left:0;top:150px;width:317px;bottom:92px">
    <div class="logo" style="position:absolute;top:12px;left:10px;flex-direction:column;gap:6px;width:94px">
      <span class="dot" style="width:34px;height:34px"></span>
      <span class="name" style="font-size:9.5px">Bramwell Co-Op</span>
    </div>
    <p class="tiny" style="position:absolute;top:14px;left:112px;right:14px">Bramwell Co-Op brings local non-profit, faith-based and community organizations together so each can do more with less. Through shared purchasing, simple billing and hands-on support, our members save money and time while building a stronger, more connected community for everyone they serve.</p>
    <div class="band" style="position:absolute;top:88px;left:0;right:0;height:26px;padding:6px 14px;font-size:11px;font-weight:700;letter-spacing:.4px">MEMBERSHIP IS THE HEART</div>
    <p class="tiny" style="position:absolute;top:122px;left:14px;right:14px">Every member strengthens the whole. Your participation increases our collective voice, lowers costs for neighbors and keeps resources circulating close to home where they do the most good.</p>
    <h2 class="benefits-heading" style="position:absolute;top:156px;left:14px;right:14px">Some of the benefits that we can offer you include...</h2>
    <div style="position:absolute;top:200px;left:10px;width:143px">
      <div class="benefit"><h4><svg width="10" height="10" viewBox="0 0 10 10"><circle cx="5" cy="5" r="4.5" fill="#3a8fd6"/><path d="M3 5.2l1.4 1.4L7.2 3.6" stroke="#fff" stroke-width="1.2" fill="none"/></svg>Discounts</h4><p>Group buying power lowers prices on supplies, insurance and utilities, with savings passed on to you.</p></div>
      <div class="benefit"><h4><svg width="10" height="10" viewBox="0 0 10 10"><circle cx="5" cy="5" r="4.5" fill="#3a8fd6"/><path d="M3 5.2l1.4 1.4L7.2 3.6" stroke="#fff" stroke-width="1.2" fill="none"/></svg>Resources</h4><p>Shared training, templates and expert guidance for budgets, buildings and staff planning.</p></div>
      <div class="benefit"><h4><svg width="10" height="10" viewBox="0 0 10 10"><circle cx="5" cy="5" r="4.5" fill="#3a8fd6"/><path d="M3 5.2l1.4 1.4L7.2 3.6" stroke="#fff" stroke-width="1.2" fill="none"/></svg>Annual Rebate</h4><p>Year-end surplus is returned to members based on how much they use the co-op.</p></div>
    </div>
    <div style="position:absolute;top:200px;left:163px;width:143px">
      <div class="benefit"><h4><svg width="10" height="10" viewBox="0 0 10 10"><circle cx="5" cy="5" r="4.5" fill="#3a8fd6"/><path d="M3 5.2l1.4 1.4L7.2 3.6" stroke="#fff" stroke-width="1.2" fill="none"/></svg>Bill Consolidation</h4><p>One clear monthly statement replaces many vendor bills and saves hours of office work.</p></div>
      <div class="benefit"><h4><svg width="10" height="10" viewBox="0 0 10 10"><circle cx="5" cy="5" r="4.5" fill="#3a8fd6"/><path d="M3 5.2l1.4 1.4L7.2 3.6" stroke="#fff" stroke-width="1.2" fill="none"/></svg>Sustainability</h4><p>Practical programs cut energy use and waste while caring for the place we call home.</p></div>
      <div class="benefit"><h4><svg width="10" height="10" viewBox="0 0 10 10"><circle cx="5" cy="5" r="4.5" fill="#3a8fd6"/><path d="M3 5.2l1.4 1.4L7.2 3.6" stroke="#fff" stroke-width="1.2" fill="none"/></svg>Local Support</h4><p>A friendly team nearby that knows your community and answers when you call.</p></div>
    </div>
  </div>

  <aside style="position:absolute;left:317px;top:150px;width:192px;bottom:92px;background:var(--gray-soft)">
    <div style="background:var(--gray)">
      <div class="list-item">Sustainability</div>
      <div class="list-item">Collaboration</div>
      <div class="list-item">Community</div>
      <div class="list-item" style="border:none">Solutions</div>
    </div>
    <div class="band" style="margin:22px 12px 0;padding:12px">
      <p style="font-size:8.5px;font-weight:700;line-height:1.35">An annual membership fee of $100 includes all of these features and more.</p>
    </div>
    <div style="padding:16px 14px">
      <p class="small">For more information or how we can provide assistance, please visit our website:</p>
      <p class="small" style="font-weight:700;color:var(--blue);margin:2px 0 10px">www.bramwellco-op.org</p>
      <p class="small">Call us at:</p>
      <p style="font-size:10px;font-weight:700;color:var(--charcoal);margin-bottom:8px">(555) 201-4470</p>
      <p class="small">Email us at:</p>
      <p class="small" style="font-weight:700;color:var(--blue)">info@bramwellco-op.org</p>
    </div>
    <div style="position:absolute;bottom:0;left:0;right:0;background:var(--blue-deep);color:var(--white);padding:12px 14px">
      <p style="font-size:8.5px;font-weight:700;line-height:1.35">We look forward to welcoming you into our cooperative community!</p>
    </div>
  </aside>

  <footer style="position:absolute;left:0;right:0;bottom:0;height:92px;background:var(--gray);display:flex;align-items:center;padding:0 18px;gap:28px">
    <div class="small"><p style="font-weight:700;color:var(--charcoal)">Bramwell Cooperative, Inc.</p><p>240 Hollis Way</p><p>Larkfield, PA 10000</p></div>
    <div class="small"><p>Phone: (555) 201-4470</p><p>Fax: (555) 201-4471</p><p>info@bramwellco-op.org</p></div>
    <p style="margin-left:auto;font-size:8px;font-weight:700;color:var(--blue)">www.bramwellco-op.org</p>
  </footer>
</section>

</body>
</html>
```